App to show who has come in an out of a room

I need an app to show who has walked in and out of a room. I want one side to say "Chamber" and the other to say "Outside". I have attached all the pictures that I want to be able to switch left or right. I don't want the picture to disappear.
I want them to be able to switch back and forth using an iPad app.
Font styles to use
Serif
Requirements
Should not have
- The pictures of the people should not dissapear. I want to someone's finger to be able to drag them back and forth.

```html
<!DOCTYPE html>
<html lang="en">
<head>
<meta charset="utf-8">
<title>Room Presence – iPad Screens</title>
<link href="https://fonts.googleapis.com/css2?family=Lato:wght@400;700&family=Lexend:wght@300;400;500&display=swap" rel="stylesheet">
<style>
  :root {
    --canvas: #cfcfcf;
    --screen: #ffffff;
    --ink: #222426;
    --muted: #5a5d60;
    --header: #262a2d;
    --header-text: #ffffff;
    --status-dim: #8b8f92;
    --accent: #e8b513;
    --board: #efefef;
    --divider: #a9abad;
    --shadow: rgba(0,0,0,0.35);
  }
  * { box-sizing: border-box; margin: 0; padding: 0; }
  html, body { width: 1200px; height: 1200px; overflow: hidden; }
  body { background: var(--canvas); position: relative; font-family: "Lexend", sans-serif; color: var(--ink); }

  .screen { position: absolute; width: 842px; height: 631px; box-shadow: 2px 3px 4px var(--shadow); overflow: hidden; }
  .splash { left: 30px; top: 22px; background: var(--screen); }
  .board { left: 280px; top: 560px; height: 632px; background: var(--board); }

  .status-bar { position: absolute; left: 0; right: 0; top: 0; height: 26px; font-family: "Lato", sans-serif; font-size: 10px; color: var(--ink); }
  .status-bar .carrier { position: absolute; left: 10px; top: 8px; display: flex; align-items: center; gap: 6px; }
  .status-bar .signal { display: flex; gap: 1.5px; }
  .status-bar .signal i { width: 5px; height: 5px; border-radius: 50%; background: currentColor; display: block; }
  .status-bar .time { position: absolute; left: 0; right: 0; top: 7px; text-align: center; }
  .status-bar .system { position: absolute; right: 12px; top: 6px; display: flex; align-items: center; gap: 5px; }
  .status-bar svg { display: block; }
  .board .status-bar { color: var(--status-dim); }

  .brand { position: absolute; left: 0; right: 0; top: 221px; text-align: center; }
  .brand .mark { width: 128px; height: 128px; border-radius: 50%; background: var(--accent); color: #fff; margin: 0 auto; display: flex; align-items: center; justify-content: center; font-weight: 300; font-size: 14px; }
  .brand .name { font-size: 25px; font-weight: 500; margin-top: 12px; letter-spacing: 0.2px; }
  .brand .tagline { font-size: 13px; font-weight: 300; letter-spacing: 11.6px; margin-top: 1px; padding-left: 8px; }

  .app-header { position: absolute; left: 0; right: 0; top: 0; height: 59px; background: var(--header); }
  .app-title { position: absolute; left: 0; right: 0; top: 33px; text-align: center; color: var(--header-text); font-size: 14.5px; font-weight: 400; }

  .refresh { position: absolute; left: 355px; top: 75px; width: 130px; height: 37px; background: var(--accent); color: #fff; border: none; border-radius: 2px; font-family: "Lexend", sans-serif; font-size: 15px; font-weight: 500; }
  .zone-title { position: absolute; top: 97px; width: 200px; text-align: center; font-size: 23px; font-weight: 400; }
  .zone-title.chamber { left: 110px; }
  .zone-title.outside { left: 530px; }
  .divider { position: absolute; left: 419px; top: 124px; width: 3px; height: 464px; background: var(--divider); border-radius: 2px; }

  .roster { position: absolute; top: 148px; display: grid; grid-template-columns: repeat(6, 66px); grid-auto-rows: 80px; list-style: none; }
  .roster.chamber { left: 9px; }
  .roster.outside { left: 433px; top: 147px; grid-auto-rows: 78.5px; }
  .member { display: flex; flex-direction: column; align-items: center; }
  .avatar { width: 45px; height: 45px; border-radius: 50%; }
  .member span { font-size: 11px; margin-top: 7px; font-weight: 400; }
  .a1 { background: radial-gradient(circle at 50% 40%, #c79a82 0 30%, #7b7068 60%, #3c3a3a); }
  .a2 { background: radial-gradient(circle at 50% 40%, #d7b8a4 0 28%, #3f6a96 55%, #1f3550); }
  .a3 { background: radial-gradient(circle at 50% 45%, #e3b79d 0 30%, #5a3a28 50%, #2f74b4); }
  .a4 { background: radial-gradient(circle at 50% 45%, #ecc7b6 0 24%, #6e3a2e 45%, #eeeaf0); }
  .a5 { background: radial-gradient(circle at 50% 40%, #5b3524 0 32%, #223b66 58%, #17253d); }
  .a6 { background: radial-gradient(circle at 50% 40%, #dcb6a0 0 26%, #2d7f94 55%, #153745); }
</style>
</head>
<body>

<section class="screen splash">
  <div class="status-bar">
    <div class="carrier"><span class="signal"><i></i><i></i><i></i><i></i><i></i></span>Carrier</div>
    <div class="time">9:41 AM</div>
    <div class="system">
      <svg width="10" height="10" viewBox="0 0 10 10"><circle cx="5" cy="5" r="4" fill="none" stroke="currentColor" stroke-width="1.2"/><rect x="3.5" y="4" width="3" height="2.5" fill="currentColor"/></svg>
      <svg width="9" height="9" viewBox="0 0 9 9"><path d="M9 0 L0 4 L4 5 L5 9 Z" fill="currentColor"/></svg>
      <svg width="10" height="10" viewBox="0 0 10 10"><circle cx="5" cy="5.5" r="3.6" fill="none" stroke="currentColor" stroke-width="1.6"/><path d="M5 3.5 V5.5 H6.5" stroke="currentColor" fill="none"/></svg>
      <span>100%</span>
      <svg width="30" height="10" viewBox="0 0 30 10"><rect x="0.5" y="0.5" width="26" height="9" fill="none" stroke="currentColor"/><rect x="2" y="2" width="23" height="6" fill="currentColor"/><rect x="27.5" y="3" width="2" height="4" fill="currentColor"/></svg>
    </div>
  </div>
  <div class="brand">
    <div class="mark">LOGO</div>
    <div class="name">Application Name</div>
    <div class="tagline">Your Tagline</div>
  </div>
</section>

<section class="screen board">
  <header class="app-header">
    <div class="status-bar">
      <div class="carrier"><span class="signal"><i></i><i></i><i></i><i></i><i></i></span>Carrier</div>
      <div class="time">9:41 AM</div>
      <div class="system">
        <svg width="10" height="10" viewBox="0 0 10 10"><circle cx="5" cy="5" r="4" fill="none" stroke="currentColor" stroke-width="1.2"/><rect x="3.5" y="4" width="3" height="2.5" fill="currentColor"/></svg>
        <svg width="9" height="9" viewBox="0 0 9 9"><path d="M9 0 L0 4 L4 5 L5 9 Z" fill="currentColor"/></svg>
        <svg width="10" height="10" viewBox="0 0 10 10"><circle cx="5" cy="5.5" r="3.6" fill="none" stroke="currentColor" stroke-width="1.6"/><path d="M5 3.5 V5.5 H6.5" stroke="currentColor" fill="none"/></svg>
        <span>100%</span>
        <svg width="30" height="10" viewBox="0 0 30 10"><rect x="0.5" y="0.5" width="26" height="9" fill="none" stroke="currentColor"/><rect x="2" y="2" width="23" height="6" fill="currentColor"/><rect x="27.5" y="3" width="2" height="4" fill="currentColor"/></svg>
      </div>
    </div>
    <h1 class="app-title">APPLICATION NAME</h1>
  </header>

  <button class="refresh">Refresh</button>
  <h2 class="zone-title chamber">Chamber</h2>
  <h2 class="zone-title outside">Outside</h2>
  <div class="divider"></div>

  <ul class="roster chamber">
    <li class="member"><div class="avatar a1" role="img" aria-label="Portrait photo of Zeller"></div><span>Zeller</span></li>
    <li class="member"><div class="avatar a2" role="img" aria-label="Portrait photo of Yardley"></div><span>Yardley</span></li>
    <li class="member"><div class="avatar a3" role="img" aria-label="Portrait photo of Winton"></div><span>Winton</span></li>
    <li class="member"><div class="avatar a4" role="img" aria-label="Portrait photo of Whitford"></div><span>Whitford</span></li>
    <li class="member"><div class="avatar a5" role="img" aria-label="Portrait photo of Wexley"></div><span>Wexley</span></li>
    <li class="member"><div class="avatar a6" role="img" aria-label="Portrait photo of Warden"></div><span>Warden</span></li>
    <li class="member"><div class="avatar a1" role="img" aria-label="Portrait photo of Zeller"></div><span>Zeller</span></li>
    <li class="member"><div class="avatar a2" role="img" aria-label="Portrait photo of Yardley"></div><span>Yardley</span></li>
    <li class="member"><div class="avatar a3" role="img" aria-label="Portrait photo of Winton"></div><span>Winton</span></li>
    <li class="member"><div class="avatar a4" role="img" aria-label="Portrait photo of Whitford"></div><span>Whitford</span></li>
    <li class="member"><div class="avatar a5" role="img" aria-label="Portrait photo of Wexley"></div><span>Wexley</span></li>
    <li class="member"><div class="avatar a6" role="img" aria-label="Portrait photo of Warden"></div><span>Warden</span></li>
    <li class="member"><div class="avatar a1" role="img" aria-label="Portrait photo of Zeller"></div><span>Zeller</span></li>
    <li class="member"><div class="avatar a2" role="img" aria-label="Portrait photo of Yardley"></div><span>Yardley</span></li>
    <li class="member"><div class="avatar a3" role="img" aria-label="Portrait photo of Winton"></div><span>Winton</span></li>
    <li class="member"><div class="avatar a4" role="img" aria-label="Portrait photo of Whitford"></div><span>Whitford</span></li>
    <li class="member"><div class="avatar a5" role="img" aria-label="Portrait photo of Wexley"></div><span>Wexley</span></li>
    <li class="member"><div class="avatar a6" role="img" aria-label="Portrait photo of Warden"></div><span>Warden</span></li>
    <li class="member"><div class="avatar a1" role="img" aria-label="Portrait photo of Zeller"></div><span>Zeller</span></li>
    <li class="member"><div class="avatar a2" role="img" aria-label="Portrait photo of Yardley"></div><span>Yardley</span></li>
    <li class="member"><div class="avatar a3" role="img" aria-label="Portrait photo of Winton"></div><span>Winton</span></li>
  </ul>

  <ul class="roster outside">
    <li class="member"><div class="avatar a1" role="img" aria-label="Portrait photo of Zeller"></div><span>Zeller</span></li>
    <li class="member"><div class="avatar a2" role="img" aria-label="Portrait photo of Yardley"></div><span>Yardley</span></li>
    <li class="member"><div class="avatar a3" role="img" aria-label="Portrait photo of Winton"></div><span>Winton</span></li>
    <li class="member"><div class="avatar a4" role="img" aria-label="Portrait photo of Whitford"></div><span>Whitford</span></li>
    <li class="member"><div class="avatar a5" role="img" aria-label="Portrait photo of Wexley"></div><span>Wexley</span></li>
    <li class="member"><div class="avatar a6" role="img" aria-label="Portrait photo of Warden"></div><span>Warden</span></li>
    <li class="member"><div class="avatar a1" role="img" aria-label="Portrait photo of Zeller"></div><span>Zeller</span></li>
    <li class="member"><div class="avatar a2" role="img" aria-label="Portrait photo of Yardley"></div><span>Yardley</span></li>
    <li class="member"><div class="avatar a3" role="img" aria-label="Portrait photo of Winton"></div><span>Winton</span></li>
    <li class="member"><div class="avatar a4" role="img" aria-label="Portrait photo of Whitford"></div><span>Whitford</span></li>
    <li class="member"><div class="avatar a5" role="img" aria-label="Portrait photo of Wexley"></div><span>Wexley</span></li>
    <li class="member"><div class="avatar a6" role="img" aria-label="Portrait photo of Warden"></div><span>Warden</span></li>
    <li class="member"><div class="avatar a1" role="img" aria-label="Portrait photo of Zeller"></div><span>Zeller</span></li>
    <li class="member"><div class="avatar a2" role="img" aria-label="Portrait photo of Yardley"></div><span>Yardley</span></li>
    <li class="member"><div class="avatar a3" role="img" aria-label="Portrait photo of Winton"></div><span>Winton</span></li>
    <li class="member"><div class="avatar a4" role="img" aria-label="Portrait photo of Whitford"></div><span>Whitford</span></li>
    <li class="member"><div class="avatar a5" role="img" aria-label="Portrait photo of Wexley"></div><span>Wexley</span></li>
    <li class="member"><div class="avatar a6" role="img" aria-label="Portrait photo of Warden"></div><span>Warden</span></li>
    <li class="member"><div class="avatar a1" role="img" aria-label="Portrait photo of Zeller"></div><span>Zeller</span></li>
    <li class="member"><div class="avatar a2" role="img" aria-label="Portrait photo of Yardley"></div><span>Yardley</span></li>
    <li class="member"><div class="avatar a3" role="img" aria-label="Portrait photo of Winton"></div><span>Winton</span></li>
    <li class="member"><div class="avatar a4" role="img" aria-label="Portrait photo of Whitford"></div><span>Whitford</span></li>
    <li class="member"><div class="avatar a5" role="img" aria-label="Portrait photo of Wexley"></div><span>Wexley</span></li>
    <li class="member"><div class="avatar a6" role="img" aria-label="Portrait photo of Warden"></div><span>Warden</span></li>
    <li class="member"><div class="avatar a1" role="img" aria-label="Portrait photo of Zeller"></div><span>Zeller</span></li>
    <li class="member"><div class="avatar a2" role="img" aria-label="Portrait photo of Yardley"></div><span>Yardley</span></li>
    <li class="member"><div class="avatar a3" role="img" aria-label="Portrait photo of Winton"></div><span>Winton</span></li>
    <li class="member"><div class="avatar a4" role="img" aria-label="Portrait photo of Whitford"></div><span>Whitford</span></li>
  </ul>
</section>

</body>
</html>
```